Business Card Revision

Need to redesign my business cards for a new professional look. We are a courier company. You can go to www.qvrunners.com to see what we do. The trucks have an old company name (Sprout) on them but that is the company we are just now
changing the name.

Target Market(s)

Potential clients. We service the automotive, plumbing, printing, air freight industries as well as many others.

Industry/Entity Type

Business

Contact Information for Business Card

QVmotion
20864 Lark Fenmore Parkway
Cincinnati, Oh 45873

Thomas R. Wendall
President

tom@qvrunners.com

Main: (513) 555-0147

```html
<!DOCTYPE html>
<html lang="en">
<head>
<meta charset="utf-8">
<title>QV Runners – Business Card</title>
<link rel="stylesheet" href="https://fonts.googleapis.com/css2?family=Lato:wght@400;700;900&display=swap">
<style>
  :root {
    --backdrop: #8f8f8f;
    --card-white: #ffffff;
    --ink-dark: #2b2b2b;
    --band-dark: #333333;
    --brand-blue: #2176bd;
    --tab-grey: #eeeeee;
    --text-light: #ffffff;
  }
  * { margin: 0; padding: 0; box-sizing: border-box; }
  html, body {
    width: 1200px;
    height: 910px;
    overflow: hidden;
    background: var(--backdrop);
    font-family: "Lato", Arial, sans-serif;
  }
  .business-card {
    position: absolute;
    left: 100px;
    top: 165px;
    width: 1000px;
    height: 580px;
    background: var(--card-white);
    overflow: hidden;
  }
  .card-shapes {
    position: absolute;
    inset: 0;
  }
  .brand {
    position: absolute;
    left: 72px;
    top: 96px;
    display: flex;
    align-items: center;
    gap: 16px;
  }
  .brand-square {
    width: 44px;
    height: 44px;
    background: var(--brand-blue);
  }
  .brand-name {
    font-weight: 900;
    font-size: 44px;
    letter-spacing: 1px;
    color: var(--brand-blue);
    text-transform: uppercase;
  }
  .person {
    position: absolute;
    right: 40px;
    top: 50px;
    text-align: right;
    color: var(--ink-dark);
  }
  .person-name {
    font-weight: 900;
    font-size: 29px;
    text-transform: uppercase;
    letter-spacing: 0.3px;
  }
  .person-title {
    font-size: 18px;
    text-transform: uppercase;
    letter-spacing: 0.5px;
    margin-top: 2px;
  }
  .contact {
    position: absolute;
    left: 70px;
    top: 452px;
    color: var(--text-light);
  }
  .contact-row {
    display: flex;
    align-items: center;
    gap: 60px;
    font-size: 21px;
  }
  .contact-item {
    display: flex;
    align-items: center;
    gap: 12px;
  }
  .contact-icon { width: 22px; height: 20px; }
  .contact-address {
    font-size: 25px;
    margin-top: 24px;
  }
</style>
</head>
<body>
  <div class="business-card">
    <svg class="card-shapes" width="1000" height="580" viewBox="0 0 1000 580" aria-hidden="true">
      <path class="name-tab" d="M640,40 L1000,40 L1000,122 L632,122 Q618,122 620,108 L626,56 Q628,40 640,40 Z" fill="var(--tab-grey)"/>
      <path class="band-accent" d="M0,406 L735,406 Q768,406 786,430 L800,450 L0,450 Z" fill="var(--brand-blue)"/>
      <path class="band-dark" d="M0,416 L732,416 Q762,416 778,438 L882,580 L0,580 Z" fill="var(--band-dark)"/>
      <path class="band-block" d="M830,416 L1000,416 L1000,580 L912,580 L816,440 Q808,416 830,416 Z" fill="var(--brand-blue)"/>
    </svg>

    <div class="brand">
      <span class="brand-square"></span>
      <span class="brand-name">QV Runners</span>
    </div>

    <div class="person">
      <div class="person-name">Thomas R. Wendall</div>
      <div class="person-title">President</div>
    </div>

    <div class="contact">
      <div class="contact-row">
        <span class="contact-item">
          <svg class="contact-icon" viewBox="0 0 22 20" aria-hidden="true">
            <path d="M2,7 Q11,0 20,7 L18,9 L15,7 L15,5 Q11,3 7,5 L7,7 L4,9 Z" fill="#fff"/>
            <rect x="4" y="10" width="14" height="9" rx="2" fill="#fff"/>
          </svg>
          (513) 555-0147
        </span>
        <span class="contact-item">
          <svg class="contact-icon" viewBox="0 0 22 20" aria-hidden="true">
            <rect x="1.5" y="3.5" width="19" height="13" fill="none" stroke="#fff" stroke-width="1.8"/>
            <path d="M1.5,3.5 L11,11 L20.5,3.5" fill="none" stroke="#fff" stroke-width="1.8"/>
          </svg>
          tom@qvrunners.com
        </span>
      </div>
      <div class="contact-address">20864 Lark Fenmore Parkway, Cincinnati, Oh 45873</div>
    </div>
  </div>
</body>
</html>
```